I’m looking for a vibrant, eye-catching package design for our new premium cannabis gummies, TALVEN. This is a high-end cannabis edible gummy made with real fruit, vegan ingredients, and powered by a THC nano emulsion — the most effective way to ingest cannabis. The package will be a square-bottom bag with child-resistant zippers (image of bag attached).

What we want from you? We want your version of what the front of the bag should look like.

The following text elements should be included within your vision of the bag

Talven - Premium Cannabis Gummy
10 pieces per bag | 10mg THC per piece | 100mg THC total
Made with real fruit
Vegan (include a vegan symbol)
Flavors: Assorted flavors (Strawberry, Mango, Pineapple, Orange, Blueberry)
Oregon cannabis icon (attached)
Net Weight 250 grams (bottom of bag)

What is needed after you win.
2 other sizes. Same look but will need to rearrange some elements of the bag. The back of the bag will be the same for all sizes. Will be legal text and nutritional info. Larger two sizes has sides, as per the attached bag. All sizes will have a bottom as well. the first size will have 5 versions for flavors. Other 2 sizes will be 1 design with "assorted flavors".

Target Market(s)

Cannabis market in Oregon

Industry/Entity Type

cannabis

Requirements
Must have
• the Marijuana universal icon for being a cannabis product.
Nice to have
• nice images of fruits
Should not have
• graphic, cartoon images that would appeal to minors.

```html
<!DOCTYPE html>
<html lang="en">
<head>
<meta charset="utf-8">
<title>Talven Premium Cannabis Gummy – Front Panel</title>
<link rel="stylesheet" href="https://fonts.googleapis.com/css2?family=Bebas+Neue&family=Playfair+Display:wght@900&family=Fraunces:opsz,wght@144,900&family=Poppins:wght@500;600&family=Mr+Dafoe&family=Alfa+Slab+One&family=Oswald:wght@400;500&display=swap">
<style>
  :root {
    --stage: #a8300c;
    --bag: #0b0b0c;
    --white: #f5f5f5;
    --rule: #bdbdbd;
    --gold: #e7c768;
    --red: #d8333a;
    --berry: #c0302a;
    --lime: #a9d63c;
    --amber: #f39a1d;
    --tangerine: #f26a1c;
    --violet: #5a3fa3;
    --thc: #d83a2a;
  }
  * { margin: 0; padding: 0; box-sizing: border-box; }
  html, body { width: 1200px; height: 1200px; overflow: hidden; background: var(--stage); }
  .stage { position: relative; width: 1200px; height: 1200px; }
  .front-panel {
    position: absolute; left: 227px; top: 0; width: 746px; height: 1200px;
    background: var(--bag); color: var(--white); text-align: center;
  }
  .zip-line { position: absolute; left: 0; right: 0; top: 39px; height: 2px; background: #2a2a2c; }
  .brand {
    position: absolute; left: 0; right: 0; top: 190px;
    font: 400 206px/1 "Bebas Neue", sans-serif; letter-spacing: -2px;
    background: linear-gradient(90deg, var(--red) 8%, var(--lime) 30%, var(--amber) 50%, var(--tangerine) 68%, var(--violet) 88%);
    -webkit-background-clip: text; background-clip: text; color: transparent;
  }
  .premium-band {
    position: absolute; left: 108px; width: 528px; top: 394px; height: 72px;
    border-top: 1.5px solid var(--rule); border-bottom: 1.5px solid var(--rule);
    display: flex; align-items: center; justify-content: space-between;
  }
  .premium-band .label { font: 900 58px/1 "Playfair Display", serif; letter-spacing: 2px; color: var(--white); }
  .stars { display: flex; gap: 8px; }
  .stars svg { width: 22px; height: 22px; fill: var(--gold); }
  .product-name {
    position: absolute; left: 0; right: 0; top: 470px;
    font: 900 116px/0.98 "Fraunces", serif; letter-spacing: -3px; color: var(--white);
  }
  .tagline {
    position: absolute; left: 0; right: 0; top: 760px;
    font: 500 27px/1 "Poppins", sans-serif; letter-spacing: 8px; color: var(--white);
  }
  .real-fruit {
    position: absolute; left: 0; right: 0; top: 782px;
    font: 400 80px/1 "Mr Dafoe", cursive;
    background: linear-gradient(90deg, var(--berry) 30%, var(--lime) 45%, var(--amber) 55%, var(--tangerine) 65%, var(--violet) 80%);
    -webkit-background-clip: text; background-clip: text; color: transparent;
  }
  .flavor-band {
    position: absolute; left: 104px; width: 538px; top: 898px; height: 30px;
    border-top: 1px solid var(--rule); border-bottom: 1px solid var(--rule);
    font: 900 16px/28px "Playfair Display", serif; letter-spacing: 6.2px; color: var(--white); white-space: nowrap;
  }
  .flavor-list {
    position: absolute; left: 108px; width: 530px; top: 942px;
    display: flex; justify-content: space-between;
    font: 400 18px/1 "Alfa Slab One", serif;
  }
  .flavor-list .strawberry { color: var(--berry); }
  .flavor-list .mango { color: var(--lime); }
  .flavor-list .pineapple { color: var(--amber); }
  .flavor-list .orange { color: var(--tangerine); }
  .flavor-list .blueberry { color: var(--violet); }
  .vegan-mark {
    position: absolute; left: 108px; top: 1012px; width: 66px; height: 66px;
    border: 3px solid var(--white); border-radius: 50%;
  }
  .dose-info { position: absolute; left: 212px; top: 1016px; text-align: left; }
  .dose-info .count { font: 500 30px/1 "Oswald", sans-serif; letter-spacing: 7px; color: var(--white); }
  .dose-info .thc { margin-top: 10px; display: flex; gap: 34px; align-items: baseline; }
  .dose-info .amount { font: 400 19px/1 "Oswald", sans-serif; color: var(--thc); }
  .dose-info .unit {
    margin-left: 8px; font: 600 10px/1 "Poppins", sans-serif; color: var(--white);
    border-bottom: 1px solid var(--rule); padding-bottom: 2px;
  }
  .cannabis-symbol {
    position: absolute; left: 571px; top: 1014px; width: 56px; height: 56px;
    background: var(--red); border-radius: 6px;
  }
</style>
</head>
<body>
<main class="stage">
  <section class="front-panel" aria-label="Talven gummy bag front">
    <div class="zip-line"></div>
    <h1 class="brand">TALVEN</h1>
    <div class="premium-band">
      <div class="stars">
        <svg viewBox="0 0 24 24"><path d="M12 2l3 7h7l-5.6 4.3 2.1 7.2L12 16.3 5.5 20.5l2.1-7.2L2 9h7z"/></svg>
        <svg viewBox="0 0 24 24"><path d="M12 2l3 7h7l-5.6 4.3 2.1 7.2L12 16.3 5.5 20.5l2.1-7.2L2 9h7z"/></svg>
      </div>
      <span class="label">PREMIUM</span>
      <div class="stars">
        <svg viewBox="0 0 24 24"><path d="M12 2l3 7h7l-5.6 4.3 2.1 7.2L12 16.3 5.5 20.5l2.1-7.2L2 9h7z"/></svg>
        <svg viewBox="0 0 24 24"><path d="M12 2l3 7h7l-5.6 4.3 2.1 7.2L12 16.3 5.5 20.5l2.1-7.2L2 9h7z"/></svg>
      </div>
    </div>
    <h2 class="product-name">Cannabis<br>Gummy</h2>
    <p class="tagline">THAT IT'S</p>
    <p class="real-fruit">Real fruit</p>
    <p class="flavor-band">OUR FLAVORS ARE ASSORTED FLAVOR</p>
    <ul class="flavor-list" style="list-style:none">
      <li class="strawberry">Strawberry</li>
      <li class="mango">Mango</li>
      <li class="pineapple">Pineapple</li>
      <li class="orange">Orange</li>
      <li class="blueberry">Blueberry</li>
    </ul>
    <div class="vegan-mark" role="img" aria-label="Vegan certification badge"></div>
    <div class="dose-info">
      <p class="count">10 PIECES PER BAG</p>
      <div class="thc">
        <p><span class="amount">10MG THC</span><span class="unit">PER PIECE</span></p>
        <p><span class="amount">100MG THC</span><span class="unit">IN BAG</span></p>
      </div>
    </div>
    <div class="cannabis-symbol" role="img" aria-label="Universal cannabis product symbol"></div>
  </section>
</main>
</body>
</html>
```